Business Card Design

i am looking a business card for a car rental company long with Taxi service also a logo.

what is the latest with my project

Industry/Entity Type

Business

Contact Information for Business Card

name of the Company is Kestrel Bay Motor Leasing and Taxi Services
Address: Harbour Lane, St. Clare's Parish Antigua
Tele# 555-0142/5550187-555-0163
Email: lorimbeck@quillmarsh.test

Font styles to use
Script

```html
<!DOCTYPE html>
<html lang="en">
<head>
<meta charset="utf-8">
<title>Kestrel Bay Motor Leasing – Business Cards</title>
<link rel="stylesheet" href="https://fonts.googleapis.com/css2?family=Source+Sans+3:wght@400;700&display=swap">
<style>
  :root {
    --page: #ffffff;
    --card-dark: #0f0f0f;
    --card-shade: #1c1c1c;
    --band-blue: #00a7e1;
    --divider: #ffffff;
    --text-light: #ffffff;
    --accent-blue: #12a9e3;
  }
  * { margin: 0; padding: 0; box-sizing: border-box; }
  html, body {
    width: 1200px; height: 1200px; overflow: hidden;
    background: var(--page);
    font-family: "Source Sans 3", Arial, sans-serif;
  }
  .canvas { position: relative; width: 1200px; height: 1200px; }
  .card {
    position: absolute; width: 612px; height: 348px;
    background: var(--band-blue); overflow: hidden;
  }
  .card--front { left: 294px; top: 216px; }
  .card--back { left: 299px; top: 604px; }
  .card__photo {
    position: absolute; left: 0; top: 0; width: 612px; height: 310px;
    background: radial-gradient(ellipse at 78% 40%, var(--card-shade) 0%, var(--card-dark) 60%);
  }
  .card__divider {
    position: absolute; left: 0; top: 310px; width: 612px; height: 2px;
    background: var(--divider);
  }
  .contact {
    position: absolute; right: 34px; list-style: none;
    color: var(--text-light); font-size: 14px; line-height: 24.5px; text-align: right;
  }
  .card--front .contact { top: 24px; }
  .card--back .contact { top: 220px; }
  .brand { position: absolute; left: 50px; color: var(--text-light); }
  .brand__name {
    font-weight: 700; font-size: 52px; line-height: 1; letter-spacing: -0.5px;
    color: var(--text-light);
  }
  .brand__tagline {
    margin: 8px 0 0 70px; font-size: 20px; font-weight: 400; color: var(--accent-blue);
  }
  .card--front .brand { top: 216px; }
  .card--back .brand { top: 96px; }
</style>
</head>
<body>
<main class="canvas">
  <section class="card card--front">
    <div class="card__photo" role="img" aria-label="Dark photograph of a car's front in shadow"></div>
    <div class="card__divider"></div>
    <ul class="contact">
      <li>555-0142/5550187-555-0163</li>
      <li>lorimbeck@quillmarsh.test</li>
      <li>Harbour Lane, St. Clare's Parish Antigua</li>
    </ul>
    <div class="brand">
      <p class="brand__name">Kestrel Bay Motor</p>
      <p class="brand__tagline">Leasing and Taxi Services</p>
    </div>
  </section>

  <section class="card card--back">
    <div class="card__photo" role="img" aria-label="Dark photograph of a car's side and wheel in shadow"></div>
    <div class="card__divider"></div>
    <div class="brand">
      <p class="brand__name">Kestrel Bay Motor</p>
      <p class="brand__tagline">Leasing and Taxi Services</p>
    </div>
    <ul class="contact">
      <li>555-0142/5550187-555-0163</li>
      <li>lorimbeck@quillmarsh.test</li>
      <li>Harbour Lane, St. Clare's Parish Antigua</li>
    </ul>
  </section>
</main>
</body>
</html>
```